Designer Instructions – Updated Referral Program Flyer

(Based on the mock-up in “Brief Layout and Instructions.pdf”)

OVERALL STYLE + LAYOUT

Maintain the same general layout, structure, and flow as the mock-up flyer (front and back).

This is an update of an older flyer, not a full redesign — keep the same sections, proportions, and overall visual feel, but with cleaner, more modern design improvements.

The final flyer should look clean, bold, professional, and high-impact, geared toward realtors, property managers, and contractors who refer work.

FRONT SIDE INSTRUCTIONS
1. Header Section

Remove the Tallow Ridge Builders logo from the top banner.
(Shown on page 1 of the PDF)

2. Main Headline

Keep the same three-line structure:
EARN
UNLIMITED
CASH

Center it, maximize impact, and increase the font size of CASH so all three words match in importance.

Make the headline bold, clean, and the main focal point.

3. Cash Incentive Box

Keep the "$500 minimum OR 10% per referral" box, but upgrade the graphics to look sharper and more modern.

Ensure the wording matches exactly what’s in the mock-up.

4. Premier Partner Program Ribbon

Clean up and modernize the "PREMIER PARTNER PROGRAM" bar while keeping the same position and structure.

Ensure the checkmark badge remains crisp and professional.

5. Supporting Icons Section

Keep the four icons/benefit boxes (Guaranteed Payout, Free Evaluations, Affordable Solutions, Industry Leaders) in the same order.

Update the icons to cleaner, more modern styles — but maintain the same meanings.

Improve alignment and spacing for sharper visual consistency.

6. Remove Icons in Contact Area

At the bottom (“CALL TEXT OR BOOK ONLINE 555-014-2796 TallowRidgeBuilders.example”), remove the phone and internet icons, as noted on page 2 of the PDF.

7. Replace All Images

I (Darnell) will provide all updated stock images separately via email.

Replace the flood/water-damage imagery and roof leak with the new images I send.

Keep image placement and proportions the same as the mock-up.

BACK SIDE INSTRUCTIONS
1. Header Image + “REFER / EARN” Section

Maintain the same large split-image layout (“The more you refer, the more you earn”).

Replace all background imagery with the new assets I will send.

Keep the CASH FLOW image section but modernize the type and spacing.

2. “HOW IT WORKS” Section

Preserve the three-column layout:

Refer Flood, Water & Mold Damage

We Take Care of Everything (evaluations/insurance)

Get Paid to Share

Update images, tighten spacing, and use modern iconography.

3. Remove Phone/Internet Icons

Same as the front side — remove small communication icons and keep only the text/number/URL.

4. Bottom Contact Bar

Keep the blue bar, same wording, same layout — just modernize the style if needed for clarity.

5. Replace All Back-Side Images

Again, I will email you the image assets.

Keep the layout EXACT — just update with higher-quality photos and improved design.

TEXT CONTENT (Keep as-is unless spacing adjustments needed)

All text shown in the PDF should remain exactly the same unless spacing or visual balance requires minor adjustments.
Example from page 3:

“REFER FLOOD, MOLD & CONSTRUCTION JOBS”

“We Schedule a Free Estimate. If Approved, You Get Paid.”

“Everybody Benefits From Referrals”

Everything stays, just refreshed and visually improved.

DESIGN GOALS

Flyer should look high-end and trustworthy, not salesy.

Consistent color theme: blues, whites, yellows, same palette as original.

Use bold, modern fonts with strong readability.

Ensure all headlines pop and all benefit boxes are clean, well-aligned, and evenly spaced.

The final result should feel like a premium referral program flyer for a top-tier restoration/remodel company.

FILES I WILL PROVIDE

I will send the designer:

All replacement stock photos

Any updated logos (if needed)

Original high-resolution version of the mock-up (if available)

Any additional icons preferred

0054AA
0677BA
7BADD7
CADEEF
E8F1F8

• Designer Instructions – Updated Referral Program Flyer (Based on the mock-up in “Brief Layout and Instructions.pdf”) OVERALL STYLE + LAYOUT Maintain the same general layout, structure, and flow as the mock-up flyer (front and back). This is an update of an older flyer, not a full redesign — keep the same sections, proportions, and overall visual feel, but with cleaner, more modern design improvements. The final flyer should look clean, bold, professional, and high-impact, geared toward realtors, property managers, and contractors who refer work. FRONT SIDE INSTRUCTIONS 1. Header Section Remove the Tallow Ridge Builders logo from the top banner. (Shown on page 1 of the PDF) 2. Main Headline Keep the same three-line structure: EARN UNLIMITED CASH Center it, maximize impact, and increase the font size of CASH so all three words match in importance. Make the headline bold, clean, and the main focal point. 3. Cash Incentive Box Keep the "$500 minimum OR 10% per referral" box, but upgrade the graphics to look sharper and more modern. Ensure the wording matches exactly what’s in the mock-up. 4. Premier Partner Program Ribbon Clean up and modernize the "PREMIER PARTNER PROGRAM" bar while keeping the same position and structure. Ensure the checkmark badge remains crisp and professional. 5. Supporting Icons Section Keep the four icons/benefit boxes (Guaranteed Payout, Free Evaluations, Affordable Solutions, Industry Leaders) in the same order. Update the icons to cleaner, more modern styles — but maintain the same meanings. Improve alignment and spacing for sharper visual consistency. 6. Remove Icons in Contact Area At the bottom (“CALL TEXT OR BOOK ONLINE 555-014-2796 TallowRidgeBuilders.example”), remove the phone and internet icons, as noted on page 2 of the PDF. 7. Replace All Images I (Darnell) will provide all updated stock images separately via email. Replace the flood/water-damage imagery and roof leak with the new images I send. Keep image placement and proportions the same as the mock-up. BACK SIDE INSTRUCTIONS 1. Header Image + “REFER / EARN” Section Maintain the same large split-image layout (“The more you refer, the more you earn”). Replace all background imagery with the new assets I will send. Keep the CASH FLOW image section but modernize the type and spacing. 2. “HOW IT WORKS” Section Preserve the three-column layout: Refer Flood, Water & Mold Damage We Take Care of Everything (evaluations/insurance) Get Paid to Share Update images, tighten spacing, and use modern iconography. 3. Remove Phone/Internet Icons Same as the front side — remove small communication icons and keep only the text/number/URL. 4. Bottom Contact Bar Keep the blue bar, same wording, same layout — just modernize the style if needed for clarity. 5. Replace All Back-Side Images Again, I will email you the image assets. Keep the layout EXACT — just update with higher-quality photos and improved design. TEXT CONTENT (Keep as-is unless spacing adjustments needed) All text shown in the PDF should remain exactly the same unless spacing or visual balance requires minor adjustments. Example from page 3: “REFER FLOOD, MOLD & CONSTRUCTION JOBS” “We Schedule a Free Estimate. If Approved, You Get Paid.” “Everybody Benefits From Referrals” Everything stays, just refreshed and visually improved. DESIGN GOALS Flyer should look high-end and trustworthy, not salesy. Consistent color theme: blues, whites, yellows, same palette as original. Use bold, modern fonts with strong readability. Ensure all headlines pop and all benefit boxes are clean, well-aligned, and evenly spaced. The final result should feel like a premium referral program flyer for a top-tier restoration/remodel company. FILES I WILL PROVIDE I will send the designer: All replacement stock photos Any updated logos (if needed) Original high-resolution version of the mock-up (if available) Any additional icons preferred

```html
<!DOCTYPE html>
<html lang="en">
<head>
<meta charset="utf-8">
<title>Premier Partner Program – Referral Flyer</title>
<link rel="stylesheet" href="https://fonts.googleapis.com/css2?family=Roboto:wght@300;400;500;700;900&family=Oswald:wght@500&display=swap">
<style>
  :root {
    --navy: #0e2a82;
    --navy-deep: #081c5e;
    --royal: #1a3d9c;
    --bar-blue: #0b2f9a;
    --yellow: #ffe500;
    --sign-yellow: #f7dc1e;
    --red: #e01b22;
    --red-dark: #c8202a;
    --slate: #7f8a95;
    --ink: #111111;
    --paper: #f6f6f8;
    --white: #ffffff;
    --text-grey: #333333;
  }
  html, body { margin: 0; padding: 0; overflow: hidden; background: var(--white); }
  .flyer {
    position: relative;
    width: 1200px; height: 780px;
    overflow: hidden;
    background: var(--paper);
    font-family: "Roboto", Arial, sans-serif;
    color: var(--ink);
  }
  .skyline-photo {
    position: absolute; left: 400px; top: 0; width: 800px; height: 304px;
    background: linear-gradient(180deg, #6c5f9e 0%, #a27aa8 30%, #d99aa0 48%, #b47f63 60%, #4e4a6a 74%, #5b5f8e 86%, #7e80a8 100%);
  }
  .hero-shapes { position: absolute; left: 0; top: 0; }
  .headline {
    position: absolute; left: 20px; top: 52px; width: 330px;
    text-align: center; font-weight: 900; line-height: 1; margin: 0;
  }
  .headline span { display: block; }
  .headline .earn { color: var(--yellow); font-size: 58px; }
  .headline .unlimited { color: var(--white); font-size: 54px; margin-top: 6px; }
  .headline .cash { color: var(--yellow); font-size: 86px; margin-top: 4px; letter-spacing: 1px; }
  .graphics { position: absolute; left: 0; top: 0; }
  .premier-label {
    position: absolute; left: 726px; top: 318px; width: 422px;
    text-align: center; font-size: 27px; font-weight: 400; letter-spacing: 9px;
  }
  .section-title {
    position: absolute; left: 51px; top: 466px; margin: 0;
    font-size: 34px; font-weight: 700; color: var(--royal);
  }
  .benefit { position: absolute; width: 340px; }
  .benefit h3 { margin: 0; font-size: 27px; font-weight: 500; letter-spacing: 0.3px; line-height: 1; }
  .benefit p { margin: 6px 0 0; font-size: 13px; color: var(--text-grey); }
  .benefit.rule { border-bottom: 1.5px dotted #777; padding-bottom: 9px; }
  .tagline {
    position: absolute; left: 50px; top: 668px; margin: 0;
    font-size: 28px; font-weight: 700; color: var(--royal);
  }
  .contact-bar {
    position: absolute; left: 16px; top: 711px; width: 826px; height: 80px;
    background: var(--bar-blue); border-radius: 26px 26px 0 0;
  }
  .web-bar {
    position: absolute; left: 821px; top: 711px; width: 357px; height: 80px;
    background: var(--ink); border-radius: 26px 26px 0 0;
  }
  .contact-cta {
    position: absolute; left: 50px; top: 725px;
    font-size: 29px; font-weight: 700; color: var(--yellow);
  }
  .contact-phone {
    position: absolute; left: 503px; top: 718px;
    font-size: 38px; font-weight: 300; color: var(--yellow);
  }
  .contact-web {
    position: absolute; left: 821px; top: 729px; width: 357px; text-align: center;
    font-size: 22px; font-weight: 400; color: var(--white);
  }
</style>
</head>
<body>
<main class="flyer">

  <div class="skyline-photo" role="img" aria-label="Evening city skyline of waterfront towers over the bay"></div>

  <svg class="hero-shapes" width="1200" height="304" viewBox="0 0 1200 304">
    <defs>
      <linearGradient id="panelBlue" x1="0" y1="0" x2="1" y2="1">
        <stop offset="0" stop-color="#0a2166"/>
        <stop offset="0.6" stop-color="#14359a"/>
        <stop offset="1" stop-color="#0c2a86"/>
      </linearGradient>
    </defs>
    <polygon points="0,0 439,0 382,146 435,304 0,304" fill="url(#panelBlue)"/>
    <polyline points="439,0 382,146 435,304" fill="none" stroke="#ffffff" stroke-width="4"/>
  </svg>

  <h1 class="headline">
    <span class="earn">EARN</span>
    <span class="unlimited">UNLIMITED</span>
    <span class="cash">CASH</span>
  </h1>

  <svg class="graphics" width="1200" height="780" viewBox="0 0 1200 780">
    <!-- hanging sign -->
    <path d="M146 290 C 132 268, 142 246, 160 228" fill="none" stroke="#ffffff" stroke-width="2.5"/>
    <polygon points="146,272 238,364 146,456 54,364" fill="var(--sign-yellow)" stroke="#2a2a1a" stroke-width="3" stroke-linejoin="round"/>
    <polygon points="146,279 231,364 146,449 61,364" fill="none" stroke="#d1b400" stroke-width="1"/>
    <circle cx="146" cy="291" r="4" fill="#2a2a1a"/>
    <text x="146" y="361" text-anchor="middle" font-family="Oswald, sans-serif" font-weight="500" font-size="36" fill="#2b2b1c" letter-spacing="-1">GET PAID</text>
    <text x="146" y="397" text-anchor="middle" font-family="Oswald, sans-serif" font-weight="500" font-size="36" fill="#2b2b1c" letter-spacing="-1">TO SHARE</text>

    <!-- cash incentive ribbon -->
    <polygon points="259,339 472,339 450,413 259,413 289,376" fill="var(--yellow)" stroke="#111" stroke-width="3" stroke-linejoin="round"/>
    <polygon points="495,339 701,339 676,376 701,413 465,413" fill="var(--yellow)" stroke="#111" stroke-width="3" stroke-linejoin="round"/>
    <polygon points="456,352 498,352 487,398 445,398" fill="var(--red)"/>
    <text x="471" y="382" text-anchor="middle" font-family="Roboto, sans-serif" font-style="italic" font-weight="900" font-size="20" fill="#fff">OR</text>
    <text x="368" y="377" text-anchor="middle" font-family="Roboto, sans-serif" font-weight="900" font-size="33" fill="var(--red)">$500</text>
    <text x="368" y="396" text-anchor="middle" font-family="Roboto, sans-serif" font-weight="700" font-size="18" fill="#111">MINIMUM</text>
    <text x="581" y="377" text-anchor="middle" font-family="Roboto, sans-serif" font-weight="900" font-size="33" fill="var(--red)">10%</text>
    <text x="581" y="400" text-anchor="middle" font-family="Roboto, sans-serif" font-weight="700" font-size="18" fill="#111">PER REFERRAL</text>

    <!-- partner program bar -->
    <rect x="726" y="356" width="215" height="60" fill="var(--red)"/>
    <rect x="941" y="356" width="207" height="60" fill="var(--slate)"/>
    <path d="M937 356 L965 366 L965 388 C965 404 953 412 937 418 C921 412 909 404 909 388 L909 366 Z" fill="#ffffff"/>
    <polyline points="925,387 934,396 950,378" fill="none" stroke="var(--red)" stroke-width="5" stroke-linecap="round" stroke-linejoin="round"/>
    <text x="825" y="398" text-anchor="middle" font-family="Roboto, sans-serif" font-weight="700" font-size="31" fill="#fff">PARTNER</text>
    <text x="1058" y="398" text-anchor="middle" font-family="Roboto, sans-serif" font-weight="700" font-size="31" fill="#fff">PROGRAM</text>

    <!-- benefit dividers -->
    <line x1="111" y1="522" x2="111" y2="642" stroke="var(--red)" stroke-width="3"/>
    <circle cx="111" cy="541" r="6" fill="var(--red)"/>
    <circle cx="111" cy="605" r="6" fill="var(--red)"/>
    <line x1="555" y1="522" x2="555" y2="642" stroke="var(--red)" stroke-width="3"/>
    <circle cx="555" cy="544" r="6" fill="var(--red)"/>
    <circle cx="555" cy="609" r="6" fill="var(--red)"/>

    <!-- icon: shield award -->
    <g fill="none" stroke="var(--red-dark)" stroke-width="2" stroke-linejoin="round">
      <path d="M69 524 L86 530 L86 546 C86 557 78 563 69 567 C60 563 52 557 52 546 L52 530 Z"/>
      <circle cx="69" cy="542" r="8"/>
      <path d="M64 549 L62 558 L66 556 M74 549 L76 558 L72 556"/>
    </g>
    <!-- icon: checklist with magnifier -->
    <g fill="none" stroke="var(--red-dark)" stroke-width="2" stroke-linejoin="round">
      <rect x="51" y="587" width="26" height="34" rx="2"/>
      <rect x="55" y="592" width="5" height="5"/><line x1="63" y1="594" x2="72" y2="594"/>
      <rect x="55" y="602" width="5" height="5"/><line x1="63" y1="604" x2="70" y2="604"/>
      <rect x="55" y="612" width="5" height="5"/>
      <circle cx="80" cy="614" r="7"/>
      <line x1="85" y1="619" x2="92" y2="626" stroke-width="3" stroke-linecap="round"/>
    </g>
    <!-- icon: hand with coin -->
    <g fill="none" stroke="var(--red-dark)" stroke-width="2" stroke-linejoin="round">
      <circle cx="514" cy="538" r="11"/>
      <text x="514" y="543" text-anchor="middle" font-family="Roboto, sans-serif" font-weight="700" font-size="13" fill="var(--red-dark)" stroke="none">$</text>
      <path d="M492 552 L502 552 C508 552 512 556 518 556 L526 556 M492 566 L506 566 L530 556 C534 554 534 550 530 550 L518 552"/>
      <rect x="486" y="549" width="6" height="20"/>
      <path d="M532 528 L536 524 L536 532 Z"/>
    </g>
    <!-- icon: team structure -->
    <g fill="none" stroke="var(--red-dark)" stroke-width="2">
      <circle cx="513" cy="595" r="6"/>
      <path d="M505 609 C505 601 521 601 521 609"/>
      <line x1="513" y1="610" x2="513" y2="615"/>
      <line x1="499" y1="615" x2="527" y2="615"/>
      <circle cx="499" cy="624" r="4"/><circle cx="513" cy="624" r="4"/><circle cx="527" cy="624" r="4"/>
      <path d="M493 633 C493 627 505 627 505 633 M507 633 C507 627 519 627 519 633 M521 633 C521 627 533 627 533 633"/>
    </g>

    <!-- emergency service seal -->
    <defs>
      <path id="sealArc" d="M974 556 A 63 63 0 0 0 1100 556"/>
    </defs>
    <circle cx="1037" cy="559" r="75" fill="#ffffff" stroke="var(--red-dark)" stroke-width="3"/>
    <circle cx="1037" cy="548" r="46" fill="var(--red-dark)"/>
    <text x="1037" y="561" text-anchor="middle" font-family="Roboto, sans-serif" font-weight="900" font-size="56" fill="#ffffff">24</text>
    <text x="1037" y="590" text-anchor="middle" font-family="Roboto, sans-serif" font-weight="900" font-size="18" fill="var(--red-dark)">HOUR</text>
    <text font-family="Roboto, sans-serif" font-weight="900" font-size="15" fill="var(--red-dark)" letter-spacing="1">
      <textPath href="#sealArc" startOffset="50%" text-anchor="middle">EMERGENCY SERVICE</textPath>
    </text>
  </svg>

  <div class="premier-label">PREMIER</div>

  <h2 class="section-title">WHY PARTNER WITH US ?</h2>

  <section class="benefit rule" style="left:141px; top:522px; width:330px;">
    <h3>GUARANTEED PAYOUT</h3>
    <p>Minimum $500 or 10% of Total Invoice Paid Fast</p>
  </section>
  <section class="benefit rule" style="left:141px; top:586px; width:330px;">
    <h3>FREE EVALUATIONS</h3>
    <p>Fast &amp; Free Inspections &amp; Written Estimates</p>
  </section>
  <section class="benefit rule" style="left:585px; top:522px; width:330px;">
    <h3>AFFORDABLE SOLUTIONS</h3>
    <p>Lowest Out of Pocket | Costs for Your Customers</p>
  </section>
  <section class="benefit" style="left:584px; top:586px; width:340px;">
    <h3>INDUSTRY LEADERS</h3>
    <p>Licensed &amp; Certified Experts | Provide 100% Guarantee</p>
  </section>

  <p class="tagline">SEND REFERRALS | GET PAID | GROW YOUR BUSINESS</p>

  <div class="contact-bar"></div>
  <div class="web-bar"></div>
  <div class="contact-cta">CALL TEXT OR BOOK ONLINE</div>
  <div class="contact-phone">555-014-2796</div>
  <div class="contact-web">TallowRidgeBuilders.example</div>

</main>
</body>
</html>
```